Business Card Design Project

We need business cards for our new business, Vantrel Optics. We specialize in aerial videography and photography via drone. Currently we are mainly focusing on real estate videography but will branch into other markets and may even host training classes for flying drones.
Updates
Cards should include:
Name
Phone Number
Email Address
Web address
We will need to customize for more than one person and would like those fields to be editable
eps file logos are uploaded now, thanks!
Target Market(s)
Real Estate Agents, hotels, rental agencies and people who have recently purchase drones
Industry/Entity Type
Videography
Font styles to use
Look and feel
Each slider illustrates characteristics of the customer's brand and the style your logo design should communicate.

```html
<!DOCTYPE html>
<html lang="en">
<head>
<meta charset="utf-8">
<title>Vantrel Optics – Business Card</title>
<link rel="stylesheet" href="https://fonts.googleapis.com/css2?family=Open+Sans:wght@400;600;700&display=swap">
<style>
  :root {
    --stage: #ecebe8;
    --card-dark: #111112;
    --card-dark-edge: #232325;
    --card-light: #ffffff;
    --ink: #222222;
    --ink-soft: #333333;
    --brand-orange: #f08a12;
    --brand-amber: #f6a623;
    --logo-grey: #d8d8d8;
    --photo-peach: #f6e3cc;
    --photo-grey: #b9bbbe;
    --band-black: #141414;
  }
  * { margin: 0; padding: 0; box-sizing: border-box; }
  html, body {
    width: 1200px; height: 784px; overflow: hidden;
    background: var(--stage);
    font-family: "Open Sans", Arial, sans-serif;
  }
  .canvas {
    position: relative; width: 1200px; height: 784px;
    display: flex; align-items: center; justify-content: center; gap: 44px;
  }
  .card {
    position: relative; width: 520px; height: 300px; overflow: hidden;
    border-radius: 3px;
    box-shadow: 0 10px 24px rgba(0,0,0,0.18);
  }

  /* Front */
  .card-front {
    background: radial-gradient(ellipse at 50% 38%, var(--card-dark-edge) 0%, var(--card-dark) 70%);
    display: flex; align-items: center; justify-content: center;
  }
  .front-brand { display: flex; align-items: center; gap: 16px; }
  .brand-mark {
    width: 46px; height: 46px; background: var(--brand-amber);
  }
  .front-brand .brand-name {
    font-weight: 700; font-size: 34px; letter-spacing: 2px;
    color: var(--logo-grey); text-transform: uppercase;
  }

  /* Back */
  .card-back { background: var(--card-light); }
  .back-brand {
    position: absolute; left: 28px; top: 44px;
    display: flex; align-items: center; gap: 12px;
  }
  .back-brand .brand-mark { width: 40px; height: 40px; }
  .back-brand .brand-name {
    font-weight: 700; font-size: 25px; letter-spacing: 1px;
    color: var(--ink); text-transform: uppercase;
  }
  .drone-photo {
    position: absolute; right: 0; top: 48px; width: 170px; height: 178px;
    background: radial-gradient(circle at 50% 50%, var(--photo-grey) 0%, #d8d4cf 45%, var(--photo-peach) 80%);
  }
  .holder {
    position: absolute; left: 28px; top: 146px;
  }
  .holder-name {
    font-size: 20px; font-weight: 600; color: var(--brand-orange); line-height: 1.1;
  }
  .holder-title {
    font-size: 11px; color: var(--ink-soft); margin-top: 2px;
  }
  .contact-list {
    list-style: none; margin-top: 14px;
  }
  .contact-list li {
    display: flex; align-items: center; gap: 7px;
    font-size: 14px; color: var(--ink); line-height: 20px;
  }
  .contact-list svg { width: 13px; height: 13px; fill: var(--brand-orange); flex: none; }
  .back-band {
    position: absolute; left: 0; bottom: 0; width: 520px; height: 60px;
  }
</style>
</head>
<body>
  <main class="canvas">
    <section class="card card-front" aria-label="Card front">
      <div class="front-brand">
        <span class="brand-mark"></span>
        <span class="brand-name">Vantrel Optics</span>
      </div>
    </section>

    <section class="card card-back" aria-label="Card back">
      <div class="back-brand">
        <span class="brand-mark"></span>
        <span class="brand-name">Vantrel Optics</span>
      </div>

      <div class="drone-photo" role="img" aria-label="Photo of a camera drone in flight"></div>

      <div class="holder">
        <p class="holder-name">Dana Merrow</p>
        <p class="holder-title">Manager</p>
        <ul class="contact-list">
          <li>
            <svg viewBox="0 0 16 16" aria-hidden="true"><path d="M3.5 1l2.5 3-1.5 2c.9 2 2.5 3.6 4.5 4.5l2-1.5 3 2.5-1.5 3C7 14 2 9 .5 3z"/></svg>
            555-210-7384
          </li>
          <li>
            <svg viewBox="0 0 16 16" aria-hidden="true"><path d="M8 0a8 8 0 100 16A8 8 0 008 0zm5.9 7h-2.5a12 12 0 00-1-4.6A6 6 0 0113.9 7zM8 2c.7.9 1.3 2.8 1.4 5H6.6C6.7 4.8 7.3 2.9 8 2zM5.6 2.4A12 12 0 004.6 7H2.1a6 6 0 013.5-4.6zM2.1 9h2.5c.1 1.7.4 3.3 1 4.6A6 6 0 012.1 9zM8 14c-.7-.9-1.3-2.8-1.4-5h2.8c-.1 2.2-.7 4.1-1.4 5zm2.4-.4c.6-1.3.9-2.9 1-4.6h2.5a6 6 0 01-3.5 4.6z"/></svg>
            www.vantreloptics.com
          </li>
          <li>
            <svg viewBox="0 0 16 16" aria-hidden="true"><path d="M0 3h16v10H0zM1.5 4.5L8 9l6.5-4.5v-.5h-13z"/></svg>
            hello@vantreloptics.com
          </li>
          <li>
            <svg viewBox="0 0 16 16" aria-hidden="true"><path d="M8 1L0 8h2v7h4.5v-4h3v4H14V8h2z"/></svg>
            48 Harlow Ave. Fenwick, NJ. 08190
          </li>
        </ul>
      </div>

      <svg class="back-band" viewBox="0 0 520 60" aria-hidden="true">
        <polygon points="0,46 520,26 520,60 0,60" fill="var(--brand-orange)"/>
        <polygon points="0,50 520,30 520,60 0,60" fill="var(--card-light)"/>
        <polygon points="0,53 520,33 520,60 0,60" fill="var(--band-black)"/>
      </svg>
    </section>
  </main>
</body>
</html>
```